BRIM Outreach Partners Business Card Rebrand

Hello Designers! We are looking for help designing our new business card to go in conjunction with our company rebrand. Unfortunately, we have an event mid June that requires we get these printed ASAP (before our new website is launched.) We have a mostly complete Brand Book which I have uploaded to this request for your reference to company information, style, fonts. I've also enclosed our logo file in .eps & .jpg. Attached is a sample business card my boss liked but said was "too simple." I made it in Canva and do not profess to be a designer. NOT FOR DESIGN REFERENCE, ONLY FOR CONTEXT Here is what our old website looks like: https://brimoutreachpartners.com/.

```html
<!DOCTYPE html>
<html lang="en">
<head>
<meta charset="utf-8">
<title>BRIM Outreach Partners – Business Card</title>
<link href="https://fonts.googleapis.com/css2?family=Outfit:wght@400;600;700&display=swap" rel="stylesheet">
<style>
  :root {
    --backdrop: #2f2f2f;
    --card-white: #ffffff;
    --brand-blue: #4db5e7;
    --ink: #111111;
  }
  * { box-sizing: border-box; margin: 0; padding: 0; }
  html, body {
    width: 1093px; height: 1200px; overflow: hidden;
    background: var(--backdrop);
    font-family: "Outfit", sans-serif;
  }
  .card {
    position: absolute;
    left: 265px;
    width: 577px;
    height: 356px;
    border-radius: 24px;
    overflow: hidden;
  }
  .card--front { top: 226px; background: var(--card-white); }
  .card--back  { top: 621px; background: var(--brand-blue); }

  .brand {
    position: absolute;
    display: flex;
    align-items: center;
    gap: 14px;
  }
  .brand__dot {
    width: 74px; height: 74px; border-radius: 50%;
    flex: none;
  }
  .brand__name {
    font-weight: 700;
    font-size: 34px;
    line-height: 1.02;
    letter-spacing: -0.5px;
  }
  .card--front .brand { right: 34px; top: 52px; }
  .card--front .brand__dot { background: var(--brand-blue); }
  .card--front .brand__name { color: var(--ink); }

  .card--back .brand { left: 50%; top: 50%; transform: translate(-50%, -50%); }
  .card--back .brand__dot { background: var(--card-white); width: 96px; height: 96px; }
  .card--back .brand__name { color: var(--card-white); font-size: 42px; }

  .person { position: absolute; left: 28px; top: 185px; }
  .person__name {
    font-weight: 700; font-size: 19px; color: var(--ink);
    text-transform: uppercase; letter-spacing: 0.2px; line-height: 1.05;
  }
  .person__role { font-size: 17px; color: var(--brand-blue); line-height: 1.1; }

  .contacts { position: absolute; left: 26px; top: 249px; list-style: none; }
  .contacts li {
    display: flex; align-items: center; gap: 8px;
    font-size: 17px; color: var(--ink); height: 25px;
  }
  .contacts svg { width: 21px; height: 21px; flex: none; }

  .front-band {
    position: absolute; left: 0; right: 0; bottom: 0; height: 12px;
    background: var(--brand-blue);
  }
</style>
</head>
<body>
  <section class="card card--front">
    <div class="brand">
      <span class="brand__dot"></span>
      <span class="brand__name">BRIM Outreach<br>Partners</span>
    </div>

    <div class="person">
      <p class="person__name">Daniel Marsh-Holt</p>
      <p class="person__role">Managing Partner</p>
    </div>

    <ul class="contacts">
      <li>
        <svg viewBox="0 0 24 24" aria-hidden="true"><circle cx="12" cy="12" r="12" fill="#4db5e7"/><path d="M8.5 6.5l2 2.5-1.2 1.3c.7 1.6 2 2.9 3.6 3.6l1.3-1.2 2.5 2-1.3 2c-4.3-.4-8.2-4.3-8.6-8.6z" fill="#fff"/></svg>
        +945-555-0142
      </li>
      <li>
        <svg viewBox="0 0 24 24" aria-hidden="true"><circle cx="12" cy="12" r="12" fill="#4db5e7"/><rect x="6" y="8" width="12" height="8.5" rx="1" fill="#fff"/><path d="M6.3 8.4L12 13l5.7-4.6" fill="none" stroke="#4db5e7" stroke-width="1.2"/></svg>
        daniel@brimoutreachpartners.com
      </li>
      <li>
        <svg viewBox="0 0 24 24" aria-hidden="true"><circle cx="12" cy="12" r="12" fill="#4db5e7"/><path d="M12 5a4.6 4.6 0 0 0-4.6 4.6c0 3.4 4.6 8.6 4.6 8.6s4.6-5.2 4.6-8.6A4.6 4.6 0 0 0 12 5z" fill="#fff"/><circle cx="12" cy="9.6" r="1.8" fill="#4db5e7"/></svg>
        Riverton, GA based (Central Time)
      </li>
    </ul>

    <div class="front-band"></div>
  </section>

  <section class="card card--back">
    <div class="brand">
      <span class="brand__dot"></span>
      <span class="brand__name">BRIM Outreach<br>Partners</span>
    </div>
  </section>
</body>
</html>
```